Overview of Elder Abuse Resources Brochure

We need a 2-page brochure that provides a list of resources for elders in tribal communities in the US and those who care for them. We want it to be simple and easy to read, and easy to see the difference between each resource. We would also like eye-catching images or graphics. Please keep the images on the front, and add any photos or graphics that depict Native American elders. We need both of our logos on the first page, in the far-right column. Please refer to the attached image for our brand colors and a font suggestion. Please keep the three columns on each page, but delete the blank pages in the document.

```html
<!DOCTYPE html>
<html lang="en">
<head>
<meta charset="utf-8">
<title>Services for Elders &amp; People Who Care for Them – Brochure</title>
<link href="https://fonts.googleapis.com/css2?family=Montserrat:wght@700;800&family=Nunito+Sans:ital,wght@0,400;0,600;0,700;1,400&display=swap" rel="stylesheet">
<style>
:root{
  --teal:#3c9ca6;
  --teal-dark:#2f8791;
  --teal-light:#56b5bd;
  --rust:#a44b40;
  --ink:#1f1f1f;
  --paper:#ffffff;
  --stage:#d8d8da;
  --gold:#c9a865;
}
*{box-sizing:border-box;margin:0;padding:0}
html,body{width:1200px;height:2190px;overflow:hidden;background:var(--stage)}
body{position:relative;font-family:"Nunito Sans",Arial,sans-serif;color:var(--ink)}
.page{position:absolute;left:30px;width:1140px;height:840px;display:flex;background:var(--paper);box-shadow:0 12px 30px rgba(0,0,0,.18)}
.page--outside{top:200px}
.page--inside{top:1150px}
.panel{position:relative;width:380px;height:100%;overflow:hidden}
.chevron-band{position:absolute;left:0;bottom:0;width:100%;height:40px;background:linear-gradient(90deg,#d9a39c,#e9e9e9 50%,#8cc4c9)}
.heading{font-family:Montserrat,Arial,sans-serif;font-weight:800;text-transform:uppercase;line-height:1.05}
p,li{font-size:15px;line-height:1.3}

/* Outside: respect panel */
.respect__wave{position:absolute;left:0;top:0;width:380px;height:140px}
.respect__title{position:absolute;left:40px;top:44px;color:#fff;font-size:24px}
.respect__bird{position:absolute;left:228px;top:28px;width:80px;height:64px;border-radius:50%;background:rgba(255,255,255,.35)}
.respect__body{position:absolute;left:40px;top:150px;right:32px}
.respect__body p{margin-bottom:16px}
.help-label{color:var(--teal);font-weight:700}
.insert-box{background:var(--rust);color:#fff;font-style:italic;border-radius:6px;padding:10px 14px;margin:0 0 16px -10px;font-size:14.5px;line-height:1.3}
.phone-red{color:var(--rust);font-weight:700}

/* Outside: mailing panel */
.mailer__frame{position:absolute;left:14px;top:14px;right:14px;bottom:54px;border:2px solid var(--teal)}
.vtext{position:absolute;writing-mode:vertical-rl;transform:rotate(180deg);font-size:15px;line-height:1.2;white-space:nowrap}
.mailer__brand{right:26px;top:30px;color:var(--teal);font-weight:700;font-size:13px}
.mailer__brand2{right:50px;top:150px;color:var(--gold);font-weight:700;font-size:13px}
.mailer__recipient{left:110px;top:350px}
.mailer__recipient strong{font-weight:700}
.mailer__web{right:26px;top:430px;color:var(--rust)}
.mailer__sender{left:26px;bottom:66px;color:var(--rust)}
.mailer__tel{right:26px;bottom:66px;color:var(--rust)}

/* Outside: cover panel */
.cover{background:var(--teal)}
.cover__brands{position:absolute;left:0;top:0;width:380px;height:170px;background:linear-gradient(180deg,#f1f1f1,#dcdcdc);display:flex;align-items:center;justify-content:center;gap:18px}
.brand-name{font-weight:700;font-size:17px;line-height:1.15;text-align:center}
.brand-name--teal{color:var(--teal-dark)}
.brand-name--gold{color:var(--gold)}
.brand-divider{width:2px;height:80px;background:var(--teal)}
.brand-mark{display:inline-block;width:12px;height:12px;background:currentColor;margin-bottom:6px}
.cover__photo{position:absolute;left:0;top:170px;width:380px;height:260px;background:linear-gradient(135deg,#6a3b2c,#3a2c2b 55%,#8a5a45)}
.cover__titlebox{position:absolute;left:20px;top:408px;width:340px;background:var(--rust);border-radius:8px;padding:14px 12px 12px;text-align:center;box-shadow:0 3px 6px rgba(0,0,0,.2)}
.cover__title{font-size:21px;line-height:1.12;color:#f6e6e2}
.cover__sub{margin-top:10px;font-size:14px;line-height:1.35;color:#f3d9d3}
.cover__list{position:absolute;left:34px;top:580px;right:26px;list-style:none}
.cover__list li{position:relative;padding:0 0 12px 24px;margin-bottom:12px;color:#fff;font-size:15px;border-bottom:1px solid rgba(255,255,255,.3)}
.cover__list li:last-child{border-bottom:none}
.cover__list li::before{content:"";position:absolute;left:0;top:5px;border-left:8px solid #fff;border-top:5px solid transparent;border-bottom:5px solid transparent}

/* Inside: stories */
.stories{background:linear-gradient(180deg,#ececec,#dedede)}
.tag{position:absolute;left:34px;top:30px;width:316px;background:var(--rust);color:#fff;border-radius:6px;padding:10px 16px;font-size:17px;box-shadow:0 3px 6px rgba(0,0,0,.2)}
.stories__list{position:absolute;left:34px;top:112px;right:30px;list-style:none}
.stories__list li{position:relative;padding-left:20px;margin-bottom:18px}
.stories__list li.bullet::before{content:"";position:absolute;left:0;top:7px;width:6px;height:6px;border-radius:50%;background:var(--teal)}
.stories__photo{position:absolute;left:0;top:470px;width:380px;height:200px;background:linear-gradient(135deg,#8a3b5f,#5c3147 45%,#b58a4c)}
.stories__help{position:absolute;left:0;top:670px;width:380px;height:130px;background:var(--rust);color:#fff;padding:18px 40px}
.stories__help span{display:block;font-size:18px;color:#f0d2cc}
.stories__help strong{display:block;font-family:Montserrat,Arial,sans-serif;font-weight:800;font-size:36px;margin-top:2px}

/* Inside: resources for elders */
.elders{background:linear-gradient(180deg,var(--teal-light),var(--teal) 60%,var(--teal-dark));color:#fff;padding:30px 32px 0}
.elders h2{font-size:18px;margin-bottom:18px}
.resource{padding-bottom:12px;margin-bottom:12px;border-bottom:1px solid rgba(255,255,255,.3)}
.resource:last-child{border-bottom:none}
.resource h3{font-weight:700;font-size:15px;line-height:1.2;margin-bottom:2px}
.resource p{font-size:14px;line-height:1.28;overflow-wrap:anywhere}

/* Inside: caregivers */
.caregivers{padding:32px 28px 0}
.caregivers h2{color:var(--teal);font-size:18px}
.caregivers__sub{color:var(--rust);font-style:italic;font-size:14px;margin:2px 0 14px}
.care-box{border:2px solid var(--teal);border-radius:10px;padding:14px 18px 6px;margin-bottom:16px}
.care-box .label{color:var(--rust);font-style:italic;font-size:14px}
.care-box .group{color:var(--teal);font-weight:700;font-size:15px;line-height:1.2;padding-bottom:10px;margin-bottom:10px;border-bottom:1px solid var(--teal)}
.care-item{margin-bottom:12px}
.care-item h3{color:var(--rust);font-weight:700;font-size:15px;line-height:1.2}
.care-item p{font-size:14px;line-height:1.28;overflow-wrap:anywhere}
</style>
</head>
<body>

<section class="page page--outside">
  <div class="panel respect">
    <svg class="respect__wave" viewBox="0 0 380 140" aria-hidden="true">
      <path d="M0 0H380Q340 100 150 112Q60 118 0 130Z" fill="var(--teal)"/>
    </svg>
    <h1 class="heading respect__title">Respect<br>for Elders</h1>
    <div class="respect__bird" role="img" aria-label="Line illustration of a dove carrying a branch"></div>
    <div class="respect__body">
      <p>Do you have concerns about an Elder, maybe you see that they are not taking care of themselves, or family only comes once a month when the Elder has money?</p>
      <p>Is an Elder telling you that they are not treated with respect or that someone is bothering them?</p>
      <p>These may be signs of Elder abuse, neglect or exploitation.</p>
      <p><span class="help-label">For help contact:</span><br>Your Tribal Social Services or Elders Department:</p>
      <div class="insert-box">insert contact information for your tribal services, law enforcement, etc.</div>
      <p>The Elder Help Finder for information on Adult Protective Services<br><span class="phone-red">1-800-555-0142</span></p>
      <p>If a serious emergency, call 911.</p>
      <p>For mental health support for yourself or an Elder, call or text 1-800-555-0188</p>
      <p>Domestic Violence Hotline<br><span class="phone-red">1.800.555.0199</span></p>
    </div>
    <div class="chevron-band" role="img" aria-label="Zigzag chevron pattern band"></div>
  </div>

  <div class="panel mailer">
    <div class="mailer__frame"></div>
    <div class="vtext mailer__brand">Northern Circle</div>
    <div class="vtext mailer__brand2">Elder Justice Network</div>
    <div class="vtext mailer__recipient"><strong>Recipient</strong><br>Street Address<br>City, ST ZIP Code</div>
    <div class="vtext mailer__web">Website<br>Email</div>
    <div class="vtext mailer__sender">Company Name<br>Street Address<br>City, ST ZIP</div>
    <div class="vtext mailer__tel">Tel Telephone<br>Fax Fax</div>
    <div class="chevron-band" role="img" aria-label="Zigzag chevron pattern band"></div>
  </div>

  <div class="panel cover">
    <div class="cover__brands">
      <div class="brand-name brand-name--teal"><span class="brand-mark"></span><br>Northern Circle<br>Aging Alliance</div>
      <div class="brand-divider"></div>
      <div class="brand-name brand-name--gold">Elder Justice<br>Network</div>
    </div>
    <div class="cover__photo" role="img" aria-label="Photo of a smiling Native American Elder woman wearing a beaded headscarf and shawl"></div>
    <div class="cover__titlebox">
      <h2 class="heading cover__title">Services for<br>Elders &amp; People Who<br>Care for Them</h2>
      <p class="cover__sub">My Mother | My Father | My Sister<br>My Grandchild | Myself</p>
    </div>
    <ul class="cover__list">
      <li>Are you caring for an Elder or a Grandchild?</li>
      <li>Are you an Elder who needs help staying at home?</li>
      <li>These programs and information can be a helpful resource.</li>
    </ul>
    <div class="chevron-band" role="img" aria-label="Zigzag chevron pattern band"></div>
  </div>
</section>

<section class="page page--inside">
  <div class="panel stories">
    <h2 class="heading tag">Do these stories sound familiar to you?</h2>
    <ul class="stories__list">
      <li class="bullet">My mother gets lost driving home from the store.</li>
      <li class="bullet">I need help getting groceries and with chores at home.</li>
      <li class="bullet">My dad wants to sleep all the time; he doesn't go out with friends anymore. He stopped drumming.</li>
      <li class="bullet">My sister is raising 3 grandchildren on her own.</li>
      <li>My son is disrespecting me. He only comes to visit when my retirement money arrives. He always asks for money.</li>
    </ul>
    <div class="stories__photo" role="img" aria-label="Photo of a Native American Elder woman in a green headscarf with a younger woman in traditional velvet clothing"></div>
    <div class="stories__help"><span>Help is available...</span><strong>1-800-555-0142</strong></div>
    <div class="chevron-band" role="img" aria-label="Zigzag chevron pattern band"></div>
  </div>

  <div class="panel elders">
    <h2 class="heading">Resources for Elders</h2>
    <div class="resource">
      <h3>Elder Help Finder</h3>
      <p>https://elderhelpfinder.example/home<br>Call or Text: 1-800-555-0142<br>Email: help@elderhelpfinder.example<br>For help finding support. Ask about services to Tribal Elders.</p>
    </div>
    <div class="resource">
      <h3>Memory Care Call Line</h3>
      <p>(24 hours 7 days a week)<br>Call 1-800-555-0177 For support for people living with dementia, caregivers, families and the public. Connect with a live person who can provide information, local resources, crisis assistance and emotional support.</p>
    </div>
    <div class="resource">
      <h3>Crisis Support Line</h3>
      <p>For mental health support, call or text 1-800-555-0188.</p>
    </div>
    <div class="resource">
      <h3>State &amp; Tribal Hotlines | Elder Justice Network</h3>
      <p>To find local resources within your tribe or state that specialize in elder abuse, neglect or exploitation, visit:<br>https://northerncircle.example/ejn/hotlines/state-tribal/</p>
    </div>
    <div class="resource">
      <h3>Kinship Native Helpline</h3>
      <p>A 24/7 safe, confidential and anonymous domestic and sexual violence helpline for Native Americans and Alaska Natives.<br>Call 1-844-555-0163<br>(1-844-555-KINS)<br>https://kinshiphelpline.example/</p>
    </div>
    <div class="chevron-band" role="img" aria-label="Zigzag chevron pattern band"></div>
  </div>

  <div class="panel caregivers">
    <h2 class="heading">Resources for Caregivers</h2>
    <p class="caregivers__sub">Caring for an Older Adult</p>
    <div class="care-box">
      <div class="care-item">
        <h3>Elder Help Finder</h3>
        <p>https://elderhelpfinder.example/home<br>Call or Text: 1-800-555-0142<br>Email: help@elderhelpfinder.example<br>For help finding support.<br>Ask about services to Tribal Elders.</p>
      </div>
      <div class="care-item">
        <h3>Memory Friends | Northern Circle Aging Alliance</h3>
        <p>An interactive educational program to better understand what dementia is and how it affects people.<br>https://northerncircle.example/memory-friends/</p>
      </div>
    </div>
    <div class="care-box">
      <p class="label">Caring for a Grandchild</p>
      <p class="group">Grandparents Raising Grand children (Kinship Care)</p>
      <div class="care-item">
        <h3>Kinfamilies.example</h3>
        <p>An interactive website that seeks to share all relevant publicly available information impacting grandfamilies.</p>
      </div>
      <div class="care-item">
        <h3>Grandparent Resources | Elder Justice Network</h3>
        <p>A list of resources for grandparents raising grandchildren.<br>https://northerncircle.example/ejn/resource/<br>grandparent-resources/</p>
      </div>
    </div>
    <div class="chevron-band" role="img" aria-label="Zigzag chevron pattern band"></div>
  </div>
</section>

</body>
</html>
```